Attorney Website Design

I need a top quality attorney website layout designed. Here are some examples of what I feel are great websites:
http://www.brelmoradivorceattorney.example/
http://www.vethomirlawfirm.example/
http://www.plexfirm.example/
http://www.harrowgatecriminaldefensefirm.example/
http://www.qzfirm.example/
http://www.tolvermoorcriminaldefensefirm.example/
http://www.drennocriminalattorneys.example/
http://www.qzfirm.example/
What we like about these sites:
• The different layers
• Subtle designs, textures, curves
• 3 dimensional
• Floating effects
• Prominent phone number
• Location of Areas of Practice
• Request A Consultation Prominent
• Right side bar with practice areas
• Badges
• Clear Calls to Action
• Dynamic/Staying Top navigation when you scroll
The project will be for a home page and then also an interior page (should be similar to home page).
I want to make it understood I am looking for a design which is not a typical "template" site which I can find anywhere for $50. This budget and project is for a "Custom" website design. Please submit designs similar in quality to the samples links I have posted. Creativity is a MUST! The best way to explain this is, I want a design that I can feel it unique and original, not something that looks like 95% of all websites out there.
Owen
I just wanted everyone to know that so far I am not to pleased with any of the designs. I am not looking for cut/pasting of other peoples websites but ORIGINAL and CREATIVE work.
Industry/Entity Type
Attorney

```html
<!DOCTYPE html>
<html lang="en">
<head>
<meta charset="utf-8">
<title>The Law Offices of Halden, Oakridge, &amp; Finch</title>
<link rel="stylesheet" href="https://fonts.googleapis.com/css2?family=Open+Sans:ital,wght@0,400;0,600;0,700;1,400&display=swap">
<style>
  :root {
    --black: #000000;
    --yellow: #ffd200;
    --panel: #ececec;
    --card: #f7f7f7;
    --card-white: #ffffff;
    --heading-grey: #6c7378;
    --text-grey: #555555;
    --band: #2b2b2b;
    --dot-grey: #9a9a9a;
  }
  * { box-sizing: border-box; margin: 0; padding: 0; }
  html, body { width: 1200px; height: 1000px; overflow: hidden; background: var(--black); }
  body { font-family: "Open Sans", Arial, sans-serif; position: relative; color: #fff; }

  .site-header { position: absolute; top: 0; left: 0; width: 1200px; height: 64px; background: var(--black); }
  .brand { position: absolute; left: 120px; top: 7px; width: 256px; text-align: center; font-size: 20px; line-height: 25px; color: #fff; }
  .main-nav { position: absolute; top: 24px; left: 0; font-size: 12px; font-weight: 600; }
  .main-nav a { position: absolute; color: #fff; text-decoration: none; white-space: nowrap; }
  .search-icon { position: absolute; left: 1048px; top: 26px; }

  .hero { position: absolute; top: 64px; left: 0; width: 1200px; height: 400px; }
  .hero-photo { position: absolute; left: 0; top: 0; width: 932px; height: 400px;
    background: linear-gradient(90deg, #6d4a2e 0%, #a8865d 25%, #e6e1d6 45%, #ece8de 55%, #9a7a52 72%, #5e3f28 100%); }
  .hero-photo::after { content: ""; position: absolute; inset: 0; background: rgba(0,0,0,0.18); }
  .hero-title { position: absolute; left: 0; width: 932px; top: 150px; text-align: center; font-size: 40px; color: #fff; z-index: 1; text-shadow: 0 1px 3px rgba(0,0,0,.4); }
  .hero-tagline { position: absolute; left: 0; width: 962px; top: 197px; text-align: center; font-size: 30px; font-style: italic; color: #fff; z-index: 1; text-shadow: 0 1px 3px rgba(0,0,0,.4); }
  .slider-arrow { position: absolute; top: 176px; width: 40px; height: 48px; background: var(--yellow); z-index: 2; display: flex; align-items: center; justify-content: center; }
  .slider-arrow.prev { left: 0; }
  .slider-arrow.next { left: 892px; }
  .location-map { position: absolute; left: 932px; top: 0; width: 268px; height: 200px; background: linear-gradient(135deg, #e9e6df, #dcdcd4 60%, #cfe0c4); }
  .call-box { position: absolute; left: 932px; top: 200px; width: 268px; height: 200px; background: var(--yellow); color: #000; overflow: hidden; }
  .call-box .call-text { position: absolute; left: 6px; top: 13px; font-size: 23px; font-weight: 600; line-height: 29px; }
  .call-box .call-phone { position: absolute; left: 9px; top: 112px; font-size: 34px; font-weight: 600; white-space: nowrap; }
  .call-box svg { position: absolute; left: 60px; top: 40px; }

  .slider-dots { position: absolute; top: 481px; left: 520px; display: flex; gap: 8px; }
  .slider-dots span { width: 48px; height: 4px; background: var(--dot-grey); }
  .slider-dots span.active { background: var(--yellow); }

  .consult-bar { position: absolute; left: 131px; top: 505px; width: 936px; height: 79px; background: var(--panel); border-radius: 2px; }
  .consult-bar h2 { position: absolute; left: 21px; top: 13px; font-size: 26px; font-weight: 600; color: #7a7f82; }
  .consult-bar p { position: absolute; left: 21px; top: 46px; font-size: 12px; color: #666; }
  .consult-button { position: absolute; left: 676px; top: 19px; width: 232px; height: 43px; background: var(--yellow); color: #000; font-size: 17px; font-weight: 600; display: flex; align-items: center; justify-content: center; border-radius: 2px; }

  .service-card { position: absolute; top: 625px; width: 216px; height: 250px; background: var(--card); border-radius: 2px; box-shadow: 0 3px 0 #d9d9d9; text-align: center; color: var(--text-grey); }
  .service-card.support { background: var(--card-white); }
  .service-card .icon { position: absolute; top: 30px; left: 0; width: 216px; display: flex; justify-content: center; }
  .service-card h3 { position: absolute; top: 93px; left: 0; width: 216px; font-size: 14px; font-weight: 700; color: var(--heading-grey); }
  .service-card .card-phone { position: absolute; top: 128px; left: 0; width: 216px; font-size: 24px; font-weight: 600; color: var(--heading-grey); }
  .service-card p { position: absolute; left: 12px; width: 192px; font-size: 12px; line-height: 16.5px; }
  .service-card .card-button { position: absolute; top: 226px; left: 30px; width: 160px; height: 43px; background: var(--yellow); color: #000; font-size: 13px; font-weight: 600; display: flex; align-items: center; justify-content: center; border-radius: 2px; }

  .why-band { position: absolute; top: 935px; left: 0; width: 1200px; height: 65px; background: var(--band); overflow: hidden; }
  .why-band h2 { position: absolute; top: 48px; left: 0; width: 1200px; text-align: center; font-size: 34px; font-weight: 700; color: var(--yellow); }
</style>
</head>
<body>

<header class="site-header">
  <div class="brand">The Law Offices of<br>Halden, Oakridge, &amp; Finch</div>
  <nav class="main-nav">
    <a style="left:460px">HOME</a>
    <a style="left:535px">ABOUT</a>
    <a style="left:607px">SERVICES</a>
    <a style="left:695px">CLIENTS</a>
    <a style="left:780px">DEVELOPMENTS</a>
    <a style="left:892px">CONTACT</a>
  </nav>
  <svg class="search-icon" width="14" height="14" viewBox="0 0 14 14"><circle cx="5.5" cy="5.5" r="4" fill="none" stroke="#fff" stroke-width="2"/><line x1="8.5" y1="8.5" x2="13" y2="13" stroke="#fff" stroke-width="2.4"/></svg>
</header>

<section class="hero">
  <div class="hero-photo" role="img" aria-label="Law library shelves lined with bound volumes around an arched niche holding a bust"></div>
  <h1 class="hero-title" style="font-weight:400">Gainesville’s Premiere Law Firm</h1>
  <p class="hero-tagline">Experience. Results. Dedication.</p>
  <div class="slider-arrow prev"><svg width="20" height="18" viewBox="0 0 20 18"><path d="M9 2 2 9l7 7M17 2l-7 7 7 7" fill="none" stroke="#fff" stroke-width="2.6"/></svg></div>
  <div class="slider-arrow next"><svg width="20" height="18" viewBox="0 0 20 18"><path d="M3 2l7 7-7 7M11 2l7 7-7 7" fill="none" stroke="#fff" stroke-width="2.6"/></svg></div>
  <div class="location-map" role="img" aria-label="Street map showing the office location"></div>
  <div class="call-box">
    <svg width="200" height="160" viewBox="0 0 200 160"><path d="M30 20c20-10 40-8 70 5l-10 25c-15-8-30-10-42-5 5 30 30 65 58 80 8-10 20-18 32-20l15 25c-25 20-45 25-70 18C45 130 15 80 30 20z" fill="none" stroke="#c9a400" stroke-width="3" opacity=".6"/></svg>
    <div class="call-text">CALL US<br>FOR A CONSULTATION<br>TODAY!</div>
    <div class="call-phone">+(203)555-0187</div>
  </div>
</section>

<div class="slider-dots"><span></span><span class="active"></span><span></span></div>

<section class="consult-bar">
  <h2>Tailor-made solutions, just a click away…</h2>
  <p>Place your request for a consultation today and our associates will respond with tailor made solutions for you</p>
  <div class="consult-button">REQUEST A CONSULTATION</div>
</section>

<article class="service-card support" style="left:131px">
  <div class="icon"><svg width="30" height="50" viewBox="0 0 30 50"><rect x="2" y="2" width="26" height="46" rx="4" fill="none" stroke="#111" stroke-width="2.4"/><line x1="2" y1="9" x2="28" y2="9" stroke="#111" stroke-width="2"/><line x1="2" y1="40" x2="28" y2="40" stroke="#111" stroke-width="2"/><circle cx="15" cy="44" r="1.6" fill="#111"/></svg></div>
  <h3>24x7 TELEPHONIC SUPPORT</h3>
  <div class="card-phone">+(203)555-0187</div>
  <p style="top:170px">Call our associates to know more about our services.</p>
  <div class="card-button">CALL US</div>
</article>

<article class="service-card" style="left:371px">
  <div class="icon"><svg width="52" height="52" viewBox="0 0 52 52"><path d="M6 12 26 4l20 8-4 8H10z" fill="none" stroke="#111" stroke-width="2.4" stroke-linejoin="round"/><circle cx="26" cy="11" r="2.5" fill="#111"/><path d="M11 22v8c0 10 7 18 15 18s15-8 15-18v-8" fill="none" stroke="#111" stroke-width="2.4"/><path d="M13 27h26v4H13z" fill="#111"/><path d="M19 40c4 3 10 3 14 0" fill="none" stroke="#111" stroke-width="2.2"/></svg></div>
  <h3>CRIMINAL DEFENSE</h3>
  <p style="top:131px">Ut eleifend libero sed neque rhoncus consequat. Maecenas tincidunt, augue et rutrum condimentum, libero lectus mattis orci, ut commodo.</p>
  <div class="card-button">Know More</div>
</article>

<article class="service-card" style="left:611px">
  <div class="icon"><svg width="54" height="52" viewBox="0 0 54 52"><path d="M2 50h50M10 50c4-9 12-13 17-13s13 4 17 13" fill="none" stroke="#111" stroke-width="2.4"/><path d="M27 37V14" stroke="#111" stroke-width="2.4"/><path d="M27 14c0-8 6-12 12-12 0 8-5 12-12 12zM27 26c-2-7-8-10-15-9 1 7 7 10 15 9z" fill="none" stroke="#111" stroke-width="2.4"/></svg></div>
  <h3>FAMILY LAW</h3>
  <p style="top:131px">Vivamus eget ante bibendum arcu vehicula ultricies. Integer venenatis mattis nisl, vitae pulvinar dui tempor non.</p>
  <div class="card-button">Know More</div>
</article>

<article class="service-card" style="left:851px">
  <div class="icon"><svg width="54" height="52" viewBox="0 0 54 52"><path d="M6 50V22C6 10 15 2 27 2s21 8 21 20v28" fill="none" stroke="#111" stroke-width="2.4"/><path d="M14 20c2-5 7-8 13-8s11 3 13 8v6c0 10-6 17-13 17s-13-7-13-17z" fill="none" stroke="#111" stroke-width="2.4"/><path d="M27 4v10M22 9h10" stroke="#111" stroke-width="2.4"/><path d="M6 50h42" stroke="#111" stroke-width="2.4"/></svg></div>
  <h3>PERSONAL INJURY</h3>
  <p style="top:131px">Astehicula ultricies. Integer venenatis mattis nisl, vitae pulvinar dui tempor non.</p>
  <div class="card-button">Know More</div>
</article>

<section class="why-band">
  <h2>WHY CHOOSE US?</h2>
</section>

</body>
</html>
```